Flyer Marbleknot

We need a 4-page flyer in A5 format. Font: Univers LT Std 45 Light Background color violet: 77/100/0/31 The following colors should be used for the design (text, graphic elements): White or green: 67/0/100/0 There is already a version this flyer. Flyer is attached. Flyer is attached. Please adopt style. The photos from the flyer may no longer be used.

```html
<!DOCTYPE html>
<html lang="de">
<head>
<meta charset="utf-8">
<title>Marbleknot Flyer</title>
<link rel="stylesheet" href="https://fonts.googleapis.com/css2?family=Lato:wght@300;400;700&family=Teko:wght@500&display=swap">
<style>
  :root {
    --stage: #2a2a2c;
    --violet: #2c0a7a;
    --violet-deep: #210660;
    --violet-soft: #4a2d96;
    --green: #5fb832;
    --green-light: #8fd066;
    --white: #ffffff;
    --white-soft: rgba(255,255,255,0.85);
    --rule: rgba(255,255,255,0.75);
  }
  * { box-sizing: border-box; margin: 0; padding: 0; }
  html, body { width: 1200px; height: 789px; overflow: hidden; }
  body {
    background: var(--stage);
    font-family: "Lato", sans-serif;
    color: var(--white);
  }
  .spread {
    position: absolute;
    left: 105px; top: 45px;
    width: 990px; height: 700px;
    display: flex;
  }
  .page {
    position: relative;
    width: 495px; height: 700px;
    background: var(--violet);
    overflow: hidden;
  }
  .page--left { border-right: 1px solid var(--violet-deep); }

  /* Left page */
  .intro {
    position: absolute; left: 48px; top: 48px; width: 400px;
    font-size: 11.5px; line-height: 1.45; font-weight: 400;
  }
  .intro p + p { margin-top: 10px; }
  .intro strong { font-weight: 700; color: var(--green-light); }
  .article-table {
    position: absolute; left: 48px; width: 400px;
    border-collapse: collapse;
    font-size: 9.5px; line-height: 1.15;
  }
  .article-table--black { top: 152px; }
  .article-table--blue { top: 262px; }
  .article-table th {
    background: var(--green); color: var(--violet-deep); text-align: left;
    font-weight: 700; padding: 4px 6px;
  }
  .article-table td {
    border: 1px solid var(--rule); padding: 1.5px 6px;
  }
  .article-table td:first-child { width: 80px; }
  .features {
    position: absolute; left: 48px; top: 392px; width: 200px;
    list-style: none; font-size: 11.5px; line-height: 1.3;
  }
  .features li { display: flex; gap: 10px; margin-bottom: 12px; }
  .features svg { flex: none; margin-top: 2px; }
  .product-photo {
    position: absolute; left: 282px; top: 425px;
    width: 170px; height: 200px; border-radius: 12px;
    background: radial-gradient(ellipse at 50% 30%, var(--green-light) 0%, var(--violet-soft) 55%, var(--violet-deep) 100%);
  }
  .footer-band {
    position: absolute; left: 0; right: 0; bottom: 40px; height: 24px;
    background: var(--green);
  }

  /* Right page */
  .title-band { position: absolute; left: 0; top: 70px; }
  .title {
    position: absolute; right: 28px; top: 84px;
    font-family: "Teko", sans-serif; font-weight: 500;
    color: var(--violet-deep); text-align: right;
    font-size: 36px; line-height: 0.85; letter-spacing: 0.5px;
    text-transform: uppercase;
  }
  .step-frame {
    position: absolute; border: 2px solid var(--white); background: var(--violet-deep);
  }
  .step-frame--measure { left: 40px; top: 180px; width: 185px; height: 225px; }
  .step-frame--mount { left: 262px; top: 200px; width: 190px; height: 245px; }
  .step-number {
    position: absolute; left: 6px; top: 6px; width: 14px; height: 14px;
    border-radius: 50%; background: var(--green); color: var(--violet-deep);
    font-size: 9px; font-weight: 700; text-align: center; line-height: 14px;
  }
  .drawing {
    position: absolute; left: 24px; top: 24px; right: 14px; bottom: 14px;
    background: linear-gradient(160deg, var(--violet-soft), var(--violet-deep));
  }
  .size-list {
    position: absolute; right: 18px; bottom: 20px;
    font-size: 10px; line-height: 1.2; text-align: right;
  }
  .warning { position: absolute; right: 10px; top: 20px; }
  .caption {
    position: absolute; font-size: 12px; line-height: 1.35; text-align: center;
    color: var(--white-soft);
  }
  .caption--measure { left: 40px; top: 418px; width: 185px; }
  .caption--mount { left: 262px; top: 458px; width: 190px; }
  .decor { position: absolute; left: 0; bottom: 0; }
</style>
</head>
<body>
<main class="spread">
  <section class="page page--left">
    <div class="intro">
      <p>Solide, rutschfest und stabil - für maximale Mobilität. Schnell und einfach an jeder Gehhilfe zu montieren, helfen sie, trittsicher durchs Leben zu gehen.</p>
      <p>Der <strong>«Aufsatz für Gehhilfen Marbleknot»</strong> — ein cleveres Produkt SWISS MADE — wird für Gehhilfen in den gängigsten Grössen angeboten.</p>
    </div>

    <table class="article-table article-table--black">
      <tr><th>Art. Nr.</th><th>Bezeichnung</th></tr>
      <tr><td>302000004</td><td>Aufsatz für Gehhilfe Marbleknot schwarz einzeln S</td></tr>
      <tr><td>302000005</td><td>Aufsatz für Gehhilfe Marbleknot schwarz einzeln M</td></tr>
      <tr><td>302000006</td><td>Aufsatz für Gehhilfe Marbleknot schwarz einzeln L</td></tr>
      <tr><td>302000024</td><td>Aufsatz für Gehhilfe Marbleknot schwarz Set à 2 Stück S</td></tr>
      <tr><td>302000025</td><td>Aufsatz für Gehhilfe Marbleknot schwarz Set à 2 Stück M</td></tr>
      <tr><td>302000026</td><td>Aufsatz für Gehhilfe Marbleknot schwarz Set à 2 Stück L</td></tr>
    </table>

    <table class="article-table article-table--blue">
      <tr><th>Art. Nr.</th><th>Bezeichnung</th></tr>
      <tr><td>302000001</td><td>Aufsatz für Gehhilfe Marbleknot blau einzeln S</td></tr>
      <tr><td>302000002</td><td>Aufsatz für Gehhilfe Marbleknot blau einzeln M</td></tr>
      <tr><td>302000003</td><td>Aufsatz für Gehhilfe Marbleknot blau einzeln L</td></tr>
      <tr><td>302000021</td><td>Aufsatz für Gehhilfe Marbleknot blau Set à 2 Stück S</td></tr>
      <tr><td>302000022</td><td>Aufsatz für Gehhilfe Marbleknot blau Set à 2 Stück M</td></tr>
      <tr><td>302000023</td><td>Aufsatz für Gehhilfe Marbleknot blau Set à 2 Stück L</td></tr>
    </table>

    <ul class="features">
      <li><svg width="14" height="14" viewBox="0 0 14 14"><circle cx="7" cy="7" r="6" fill="none" stroke="#5fb832" stroke-width="1.2"/><path d="M4 7.2l2 2 4-4.4" fill="none" stroke="#5fb832" stroke-width="1.4"/></svg>Metallkomponenten aus rostfreiem Stahl</li>
      <li><svg width="14" height="14" viewBox="0 0 14 14"><circle cx="7" cy="7" r="6" fill="none" stroke="#5fb832" stroke-width="1.2"/><path d="M4 7.2l2 2 4-4.4" fill="none" stroke="#5fb832" stroke-width="1.4"/></svg>Spezielles Sohlenmaterial für maximalen Halt auch auf nassen und rutschigen Böden</li>
      <li><svg width="14" height="14" viewBox="0 0 14 14"><circle cx="7" cy="7" r="6" fill="none" stroke="#5fb832" stroke-width="1.2"/><path d="M4 7.2l2 2 4-4.4" fill="none" stroke="#5fb832" stroke-width="1.4"/></svg>Profil für mehr Halt</li>
    </ul>

    <div class="footer-band"></div>
    <div class="product-photo" role="img" aria-label="Produktfoto: Gehhilfenaufsatz mit Klemmbride und Vierfuss"></div>
  </section>

  <section class="page page--right">
    <svg class="title-band" width="495" height="140" viewBox="0 0 495 140">
      <polygon points="20,40 110,0 495,0 495,140 400,140" fill="#5fb832"/>
      <polygon points="20,40 110,0 495,0 495,10 125,10" fill="#8fd066"/>
    </svg>
    <h1 class="title">Marbleknot<br>Gebrauchsanweisung</h1>

    <div class="step-frame step-frame--measure">
      <span class="step-number">1</span>
      <div class="drawing" role="img" aria-label="Strichzeichnung: Messen des Schaftdurchmessers am unteren Rohrende"></div>
      <p class="size-list">16-18 mm (S)<br>19-21 mm (M)<br>22-24 mm (L)</p>
    </div>
    <p class="caption caption--measure">Zur Grössenbestimmung den Schaft-Durchmesser im unteren Teil der Gehhilfe messen.</p>

    <div class="step-frame step-frame--mount">
      <span class="step-number">2</span>
      <div class="drawing" role="img" aria-label="Strichzeichnung: Aufsatz wird auf das Krückenrohr gesteckt und verschraubt"></div>
      <svg class="warning" width="26" height="23" viewBox="0 0 26 23"><polygon points="13,1 25,22 1,22" fill="#5fb832"/><rect x="12" y="8" width="2" height="8" fill="#210660"/><rect x="12" y="18" width="2" height="2" fill="#210660"/></svg>
    </div>
    <p class="caption caption--mount">Den Gehhilfeaufsatz so auf das Krückenrohr stecken, dass die Klemmlaschen der Bride, in Gehrichtung betrachtet, nach hinten zeigen. Die Schraube mit dem mitgelieferten Inbusschlüssel anziehen.</p>

    <svg class="decor" width="495" height="190" viewBox="0 0 495 190">
      <polygon points="0,30 75,45 140,175 60,190 0,190" fill="#5fb832"/>
      <rect x="60" y="100" width="45" height="38" fill="#8fd066"/>
      <rect x="145" y="75" width="42" height="40" fill="#ffffff"/>
      <polyline points="190,120 240,105 275,150" fill="none" stroke="#8fd066" stroke-width="7"/>
      <polygon points="300,175 355,150 395,190 310,190" fill="#4a2d96"/>
      <rect x="325" y="160" width="25" height="20" fill="#ffffff" opacity="0.6"/>
    </svg>
  </section>
</main>
</body>
</html>
```